Bright Meadow Groves - Gourmet/Specialty Snack Food Packaging Product Line

We need packaging design for a new company in Portland Oregon called Bright Meadow Groves. We import single origin, ethically sourced cashew products that are refined sugar, wheat and dairy free. Our initial product, Sunkept Pantry Nuts, is in distribution in the Pacific NW in Tallgrain Mart, Corvel Grocer and other retail chains. The final design should communicate healthy, delicious snacks that are sustainable with a strong social mission. www.brightmeadowgroves.example https://www.videohost.example/watch?v=Qm7TzRb2KpW

Target Market(s)

28-45 yo women, concerned about transparency in their food chain and want to connect with the social and environmental impacts in their purchases.

Industry/Entity Type

Product

Font styles to use
Sans Serif

Requirements
Must have
• Existing logo, full-color photograph placement on label. Call outs for "sugar-free, gluten-free, dairy free" Placement for possible certifications (GMO, organic, fair trade). Consistent "design template" to apply across multiple products ( Raw Cashews, Cacao Cashews, Salted/Roasted). Space At Bottom for "1lb (16oz)" or other weights
Nice to have
• clean designs, white background..
Should not have
• Please see attached designs and distinguish yourself from them.

```html
<!DOCTYPE html>
<html lang="en">
<head>
<meta charset="utf-8">
<title>Bright Meadow Groves – Sunkept Pantry Nuts Pouches</title>
<link rel="stylesheet" href="https://fonts.googleapis.com/css2?family=Bebas+Neue&family=Raleway:wght@500&display=swap">
<style>
  :root {
    --page-bg: #f4f4f4;
    --navy: #0b0b4f;
    --navy-accent: #1aa3e4;
    --navy-photo-deep: #1f3f86;
    --navy-photo-dark: #4f74c0;
    --navy-photo-mid: #86a3dc;
    --navy-photo-light: #dfe8f8;
    --maroon: #470404;
    --maroon-accent: #e3958c;
    --maroon-photo-deep: #7a1f1c;
    --maroon-photo-dark: #b9544e;
    --maroon-photo-mid: #dc8a80;
    --maroon-photo-light: #f8d8d2;
    --nut-dark: #b88a45;
    --nut-light: #efd7a5;
    --white: #ffffff;
  }
  * { box-sizing: border-box; margin: 0; padding: 0; }
  html, body { width: 1200px; height: 1000px; overflow: hidden; }
  body { background: var(--page-bg); position: relative; }

  .pouch {
    position: absolute;
    top: 130px;
    width: 455px;
    height: 710px;
    background: var(--band);
    overflow: hidden;
  }
  .pouch--blue {
    left: 120px;
    --band: var(--navy);
    --accent: var(--navy-accent);
    --photo-deep: var(--navy-photo-deep);
    --photo-dark: var(--navy-photo-dark);
    --photo-mid: var(--navy-photo-mid);
    --photo-light: var(--navy-photo-light);
    --ring: var(--navy-accent);
  }
  .pouch--red {
    left: 625px;
    --band: var(--maroon);
    --accent: var(--maroon-accent);
    --photo-deep: var(--maroon-photo-deep);
    --photo-dark: var(--maroon-photo-dark);
    --photo-mid: var(--maroon-photo-mid);
    --photo-light: var(--maroon-photo-light);
    --ring: var(--white);
  }

  .brand {
    position: absolute;
    top: 78px;
    left: 0;
    width: 100%;
    display: flex;
    flex-direction: column;
    align-items: center;
    gap: 14px;
  }
  .brand__dot {
    width: 58px;
    height: 58px;
    border-radius: 50%;
    background: var(--accent);
  }
  .brand__name {
    font-family: "Raleway", sans-serif;
    font-weight: 500;
    font-size: 19px;
    color: var(--accent);
  }

  .product-title {
    position: absolute;
    top: 192px;
    left: 0;
    width: 100%;
    text-align: center;
    font-family: "Bebas Neue", sans-serif;
    font-weight: 400;
    font-size: 44px;
    letter-spacing: 1px;
    color: var(--white);
  }

  .accent-stripe {
    position: absolute;
    top: 243px;
    left: 0;
    width: 100%;
    height: 8px;
    background: var(--accent);
  }

  .hero-photo {
    position: absolute;
    top: 258px;
    left: 0;
    width: 100%;
    height: 432px;
    background:
      radial-gradient(ellipse 28% 30% at 30% 72%, var(--photo-mid) 0%, transparent 100%),
      radial-gradient(ellipse 22% 30% at 58% 70%, var(--photo-mid) 0%, transparent 100%),
      radial-gradient(ellipse 30% 22% at 88% 62%, var(--photo-light) 0%, transparent 100%),
      radial-gradient(ellipse 35% 25% at 15% 20%, var(--photo-light) 0%, transparent 100%),
      radial-gradient(ellipse 40% 30% at 10% 95%, var(--photo-deep) 0%, transparent 100%),
      linear-gradient(165deg, var(--photo-mid) 0%, var(--photo-dark) 45%, var(--photo-deep) 75%, var(--photo-dark) 100%);
  }

  .callout-badge {
    position: absolute;
    left: 240px;
    top: 280px;
    width: 200px;
    height: 200px;
  }
  .callout-badge text {
    font-family: "Bebas Neue", sans-serif;
    font-size: 17px;
    letter-spacing: 0.5px;
    fill: var(--white);
  }

  .cert-marks {
    position: absolute;
    left: 28px;
    top: 636px;
    display: flex;
    gap: 10px;
  }
  .cert-marks__slot {
    width: 36px;
    height: 36px;
    border-radius: 50%;
    background: var(--white);
    opacity: 0.85;
  }

  .net-weight {
    position: absolute;
    right: 46px;
    top: 648px;
    font-family: "Bebas Neue", sans-serif;
    font-size: 20px;
    color: var(--white);
  }
</style>
</head>
<body>

<section class="pouch pouch--blue">
  <div class="brand">
    <span class="brand__dot"></span>
    <span class="brand__name">Bright Meadow Groves</span>
  </div>
  <h1 class="product-title">Sunkept Pantry Nuts</h1>
  <div class="accent-stripe"></div>
  <div class="hero-photo" role="img" aria-label="Full-bleed photo of two cashew fruits hanging on a branch among leaves, tinted blue"></div>
  <svg class="callout-badge" viewBox="-100 -100 200 200">
    <defs>
      <radialGradient id="nutsBlue" cx="50%" cy="45%" r="60%">
        <stop offset="0" stop-color="var(--nut-light)"/>
        <stop offset="1" stop-color="var(--nut-dark)"/>
      </radialGradient>
      <path id="arcBlue" d="M -67.7 24.6 A 72 72 0 1 1 67.7 24.6"/>
    </defs>
    <circle r="62" fill="var(--ring)"/>
    <circle r="56" fill="url(#nutsBlue)" role="img" aria-label="Close-up photo of raw cashew nuts"/>
    <text><textPath href="#arcBlue">SUGAR FREE - GLUTEN FREE - DAIRY FREE</textPath></text>
  </svg>
  <div class="cert-marks" aria-label="Certification mark placements">
    <span class="cert-marks__slot"></span>
    <span class="cert-marks__slot"></span>
    <span class="cert-marks__slot"></span>
  </div>
  <div class="net-weight">1LB (16OZ)</div>
</section>

<section class="pouch pouch--red">
  <div class="brand">
    <span class="brand__dot"></span>
    <span class="brand__name">Bright Meadow Groves</span>
  </div>
  <h1 class="product-title">Sunkept Pantry Nuts</h1>
  <div class="accent-stripe"></div>
  <div class="hero-photo" role="img" aria-label="Full-bleed photo of two cashew fruits hanging on a branch among leaves, tinted red"></div>
  <svg class="callout-badge" viewBox="-100 -100 200 200">
    <defs>
      <radialGradient id="nutsRed" cx="50%" cy="45%" r="60%">
        <stop offset="0" stop-color="var(--nut-light)"/>
        <stop offset="1" stop-color="var(--nut-dark)"/>
      </radialGradient>
      <path id="arcRed" d="M -67.7 24.6 A 72 72 0 1 1 67.7 24.6"/>
    </defs>
    <circle r="62" fill="var(--ring)"/>
    <circle r="56" fill="url(#nutsRed)" role="img" aria-label="Close-up photo of raw cashew nuts"/>
    <text><textPath href="#arcRed">SUGAR FREE - GLUTEN FREE - DAIRY FREE</textPath></text>
  </svg>
  <div class="cert-marks" aria-label="Certification mark placements">
    <span class="cert-marks__slot"></span>
    <span class="cert-marks__slot"></span>
    <span class="cert-marks__slot"></span>
  </div>
  <div class="net-weight">1LB (16OZ)</div>
</section>

</body>
</html>
```